Ravelor Global Kft. is an online recruitment marketplace connecting the employers and recruiters together. We provide an e-bussiness solution for companies and give busines opportunity for recruiters.
We have a logo design already, which should be used on the business card.
Our colours are grey and magenta, which can be seen in the logo. Black is also welcome.
The style should be dynamic, young but professional. It should be clear, visible, elegant, not too crowded, simple but exciting.
We need the following data on the BC: name, title, address, phone,fax and mobile number, email address, website.
Target Market(s)
Our target market are companies, as this is a B2B business. We also target recruiters, recruitment professionals, headhunters.We would like to be impressive and different.
Industry/Entity Type
Business
Requirements
Must have
- We would like to promote our website, www.ravelorglb.hu.
- Please, put this on the back with a quite visible letter size.The style should be dynamic, young but professional. It should be clear, visible, elegant, not too crowded, simple but exciting.
Should not have
- We do not want to see people figures.

```html
<!DOCTYPE html>
<html lang="en">
<head>
<meta charset="utf-8">
<title>Ravelor Global Kft. – Business Card Sheet</title>
<link rel="stylesheet" href="https://fonts.googleapis.com/css2?family=Anton&family=Tinos:ital,wght@0,700;1,400&display=swap">
<style>
  :root {
    --sheet: #ffffff;
    --card-light: #e6e9e9;
    --card-light-edge: #d3d7d8;
    --magenta: #a8168f;
    --band: #857aa3;
    --band-edge: #6f6390;
    --white: #ffffff;
    --label: #f2c9e8;
  }
  * { box-sizing: border-box; margin: 0; padding: 0; }
  html, body {
    width: 858px; height: 1200px; overflow: hidden;
    background: var(--sheet);
  }
  .sheet {
    width: 858px; height: 1200px;
    display: grid;
    grid-template-columns: 401px 401px;
    grid-template-rows: repeat(5, 226px);
    column-gap: 50px;
    row-gap: 16px;
    padding: 0 3px;
  }
  .card {
    position: relative;
    width: 401px; height: 226px;
    overflow: hidden;
  }
  .card__face {
    position: absolute; left: 0; top: 0;
    width: 401px; height: 154px;
    background: linear-gradient(180deg, var(--card-light) 0%, var(--card-light-edge) 100%);
  }
  .card__band {
    position: absolute; left: 0; top: 158px;
    width: 401px; height: 68px;
    background: linear-gradient(180deg, var(--band) 0%, var(--band-edge) 100%);
    display: flex; align-items: center; justify-content: center;
  }
  .card__website {
    font-family: "Tinos", "Times New Roman", serif;
    font-weight: 700;
    font-size: 26px;
    letter-spacing: 0.5px;
    color: var(--white);
  }
  .brand {
    position: absolute; left: 8px; top: 58px;
    font-family: "Anton", "Impact", sans-serif;
    font-size: 40px;
    line-height: 0.98;
    color: var(--magenta);
    text-transform: uppercase;
    letter-spacing: 0.5px;
  }
  .panel {
    position: absolute; left: 222px; top: 0;
    width: 179px; height: 150px;
    background: var(--magenta);
    color: var(--white);
    font-family: "Tinos", "Times New Roman", serif;
  }
  .panel__name {
    margin-top: 20px;
    text-align: center;
    font-weight: 700;
    font-size: 17px;
    letter-spacing: 0.3px;
  }
  .panel__role {
    text-align: center;
    font-style: italic;
    font-size: 9px;
    color: var(--label);
    margin-top: 1px;
  }
  .contacts {
    list-style: none;
    margin: 14px 0 0 14px;
    font-weight: 700;
    font-size: 9px;
    line-height: 11.5px;
    white-space: nowrap;
  }
  .contacts__key {
    display: inline-block; width: 14px;
    color: var(--label);
  }
</style>
</head>
<body>
<main class="sheet">
  <section class="card">
    <div class="card__face" role="img" aria-label="light grey jigsaw puzzle texture"></div>
    <div class="card__band" role="img" aria-label="purple-grey jigsaw puzzle texture"><span class="card__website">www.ravelorglb.hu</span></div>
    <div class="brand">Ravelor<br>Global</div>
    <div class="panel">
      <p class="panel__name">PROJECT OWNER</p>
      <p class="panel__role">owner or position</p>
      <ul class="contacts">
        <li><span class="contacts__key">A.</span>PO Box 2048, Budapest, 1051</li>
        <li><span class="contacts__key">P.</span>(604) 555-0142</li>
        <li><span class="contacts__key">F.</span>(604) 555-0187</li>
        <li><span class="contacts__key">M.</span>(604) 555-0163</li>
        <li><span class="contacts__key">@.</span>myname@ravelorglb.hu</li>
        <li><span class="contacts__key">W.</span>www.ravelorglb.hu</li>
      </ul>
    </div>
  </section>
  <section class="card">
    <div class="card__face" role="img" aria-label="light grey jigsaw puzzle texture"></div>
    <div class="card__band" role="img" aria-label="purple-grey jigsaw puzzle texture"><span class="card__website">www.ravelorglb.hu</span></div>
    <div class="brand">Ravelor<br>Global</div>
    <div class="panel">
      <p class="panel__name">PROJECT OWNER</p>
      <p class="panel__role">owner or position</p>
      <ul class="contacts">
        <li><span class="contacts__key">A.</span>PO Box 2048, Budapest, 1051</li>
        <li><span class="contacts__key">P.</span>(604) 555-0142</li>
        <li><span class="contacts__key">F.</span>(604) 555-0187</li>
        <li><span class="contacts__key">M.</span>(604) 555-0163</li>
        <li><span class="contacts__key">@.</span>myname@ravelorglb.hu</li>
        <li><span class="contacts__key">W.</span>www.ravelorglb.hu</li>
      </ul>
    </div>
  </section>
  <section class="card">
    <div class="card__face" role="img" aria-label="light grey jigsaw puzzle texture"></div>
    <div class="card__band" role="img" aria-label="purple-grey jigsaw puzzle texture"><span class="card__website">www.ravelorglb.hu</span></div>
    <div class="brand">Ravelor<br>Global</div>
    <div class="panel">
      <p class="panel__name">PROJECT OWNER</p>
      <p class="panel__role">owner or position</p>
      <ul class="contacts">
        <li><span class="contacts__key">A.</span>PO Box 2048, Budapest, 1051</li>
        <li><span class="contacts__key">P.</span>(604) 555-0142</li>
        <li><span class="contacts__key">F.</span>(604) 555-0187</li>
        <li><span class="contacts__key">M.</span>(604) 555-0163</li>
        <li><span class="contacts__key">@.</span>myname@ravelorglb.hu</li>
        <li><span class="contacts__key">W.</span>www.ravelorglb.hu</li>
      </ul>
    </div>
  </section>
  <section class="card">
    <div class="card__face" role="img" aria-label="light grey jigsaw puzzle texture"></div>
    <div class="card__band" role="img" aria-label="purple-grey jigsaw puzzle texture"><span class="card__website">www.ravelorglb.hu</span></div>
    <div class="brand">Ravelor<br>Global</div>
    <div class="panel">
      <p class="panel__name">PROJECT OWNER</p>
      <p class="panel__role">owner or position</p>
      <ul class="contacts">
        <li><span class="contacts__key">A.</span>PO Box 2048, Budapest, 1051</li>
        <li><span class="contacts__key">P.</span>(604) 555-0142</li>
        <li><span class="contacts__key">F.</span>(604) 555-0187</li>
        <li><span class="contacts__key">M.</span>(604) 555-0163</li>
        <li><span class="contacts__key">@.</span>myname@ravelorglb.hu</li>
        <li><span class="contacts__key">W.</span>www.ravelorglb.hu</li>
      </ul>
    </div>
  </section>
  <section class="card">
    <div class="card__face" role="img" aria-label="light grey jigsaw puzzle texture"></div>
    <div class="card__band" role="img" aria-label="purple-grey jigsaw puzzle texture"><span class="card__website">www.ravelorglb.hu</span></div>
    <div class="brand">Ravelor<br>Global</div>
    <div class="panel">
      <p class="panel__name">PROJECT OWNER</p>
      <p class="panel__role">owner or position</p>
      <ul class="contacts">
        <li><span class="contacts__key">A.</span>PO Box 2048, Budapest, 1051</li>
        <li><span class="contacts__key">P.</span>(604) 555-0142</li>
        <li><span class="contacts__key">F.</span>(604) 555-0187</li>
        <li><span class="contacts__key">M.</span>(604) 555-0163</li>
        <li><span class="contacts__key">@.</span>myname@ravelorglb.hu</li>
        <li><span class="contacts__key">W.</span>www.ravelorglb.hu</li>
      </ul>
    </div>
  </section>
  <section class="card">
    <div class="card__face" role="img" aria-label="light grey jigsaw puzzle texture"></div>
    <div class="card__band" role="img" aria-label="purple-grey jigsaw puzzle texture"><span class="card__website">www.ravelorglb.hu</span></div>
    <div class="brand">Ravelor<br>Global</div>
    <div class="panel">
      <p class="panel__name">PROJECT OWNER</p>
      <p class="panel__role">owner or position</p>
      <ul class="contacts">
        <li><span class="contacts__key">A.</span>PO Box 2048, Budapest, 1051</li>
        <li><span class="contacts__key">P.</span>(604) 555-0142</li>
        <li><span class="contacts__key">F.</span>(604) 555-0187</li>
        <li><span class="contacts__key">M.</span>(604) 555-0163</li>
        <li><span class="contacts__key">@.</span>myname@ravelorglb.hu</li>
        <li><span class="contacts__key">W.</span>www.ravelorglb.hu</li>
      </ul>
    </div>
  </section>
  <section class="card">
    <div class="card__face" role="img" aria-label="light grey jigsaw puzzle texture"></div>
    <div class="card__band" role="img" aria-label="purple-grey jigsaw puzzle texture"><span class="card__website">www.ravelorglb.hu</span></div>
    <div class="brand">Ravelor<br>Global</div>
    <div class="panel">
      <p class="panel__name">PROJECT OWNER</p>
      <p class="panel__role">owner or position</p>
      <ul class="contacts">
        <li><span class="contacts__key">A.</span>PO Box 2048, Budapest, 1051</li>
        <li><span class="contacts__key">P.</span>(604) 555-0142</li>
        <li><span class="contacts__key">F.</span>(604) 555-0187</li>
        <li><span class="contacts__key">M.</span>(604) 555-0163</li>
        <li><span class="contacts__key">@.</span>myname@ravelorglb.hu</li>
        <li><span class="contacts__key">W.</span>www.ravelorglb.hu</li>
      </ul>
    </div>
  </section>
  <section class="card">
    <div class="card__face" role="img" aria-label="light grey jigsaw puzzle texture"></div>
    <div class="card__band" role="img" aria-label="purple-grey jigsaw puzzle texture"><span class="card__website">www.ravelorglb.hu</span></div>
    <div class="brand">Ravelor<br>Global</div>
    <div class="panel">
      <p class="panel__name">PROJECT OWNER</p>
      <p class="panel__role">owner or position</p>
      <ul class="contacts">
        <li><span class="contacts__key">A.</span>PO Box 2048, Budapest, 1051</li>
        <li><span class="contacts__key">P.</span>(604) 555-0142</li>
        <li><span class="contacts__key">F.</span>(604) 555-0187</li>
        <li><span class="contacts__key">M.</span>(604) 555-0163</li>
        <li><span class="contacts__key">@.</span>myname@ravelorglb.hu</li>
        <li><span class="contacts__key">W.</span>www.ravelorglb.hu</li>
      </ul>
    </div>
  </section>
  <section class="card">
    <div class="card__face" role="img" aria-label="light grey jigsaw puzzle texture"></div>
    <div class="card__band" role="img" aria-label="purple-grey jigsaw puzzle texture"><span class="card__website">www.ravelorglb.hu</span></div>
    <div class="brand">Ravelor<br>Global</div>
    <div class="panel">
      <p class="panel__name">PROJECT OWNER</p>
      <p class="panel__role">owner or position</p>
      <ul class="contacts">
        <li><span class="contacts__key">A.</span>PO Box 2048, Budapest, 1051</li>
        <li><span class="contacts__key">P.</span>(604) 555-0142</li>
        <li><span class="contacts__key">F.</span>(604) 555-0187</li>
        <li><span class="contacts__key">M.</span>(604) 555-0163</li>
        <li><span class="contacts__key">@.</span>myname@ravelorglb.hu</li>
        <li><span class="contacts__key">W.</span>www.ravelorglb.hu</li>
      </ul>
    </div>
  </section>
  <section class="card">
    <div class="card__face" role="img" aria-label="light grey jigsaw puzzle texture"></div>
    <div class="card__band" role="img" aria-label="purple-grey jigsaw puzzle texture"><span class="card__website">www.ravelorglb.hu</span></div>
    <div class="brand">Ravelor<br>Global</div>
    <div class="panel">
      <p class="panel__name">PROJECT OWNER</p>
      <p class="panel__role">owner or position</p>
      <ul class="contacts">
        <li><span class="contacts__key">A.</span>PO Box 2048, Budapest, 1051</li>
        <li><span class="contacts__key">P.</span>(604) 555-0142</li>
        <li><span class="contacts__key">F.</span>(604) 555-0187</li>
        <li><span class="contacts__key">M.</span>(604) 555-0163</li>
        <li><span class="contacts__key">@.</span>myname@ravelorglb.hu</li>
        <li><span class="contacts__key">W.</span>www.ravelorglb.hu</li>
      </ul>
    </div>
  </section>
</main>
</body>
</html>
```